Web Design Project

We are re-starting this project.

This project is for a totally new look and design of a website for Wozzlent. www.wozzlent-example.com.

Wozzlent is a naming protocol for physical locations and can be used for fixed and mobile people, places and things. Find your friends, or find a business. Because Wozzlent locations point to precise geo-physical (GPS) co-ordinates, navigation to a location becomes totally reliable.
Updates

Please see the modified brief for this project

Target Market(s)

Every person and every business can have multiple !Wozzs (Wozzlent locations), so the website needs to be appealing and fun, but easy to use and functional

Industry/Entity Type

Business

Colors
34a6d7

Requirements
Must have
• Uniqueness!

```html
<!DOCTYPE html>
<html lang="en">
<head>
<meta charset="utf-8">
<title>Wozzlent – Who would you like to find?</title>
<link rel="stylesheet" href="https://fonts.googleapis.com/css2?family=Space+Mono:wght@400;700&family=Montserrat:wght@500&display=swap">
<style>
  :root {
    --brand-blue: #34a6d7;
    --brand-blue-deep: #2a8fc0;
    --brand-blue-edge: #2382b5;
    --signup-green: #5fd12d;
    --screen-green: #4fbf26;
    --screen-green-light: #6fd145;
    --callout-pink: #f0155f;
    --ink: #111111;
    --white: #ffffff;
    --field-bg: #f4f9fc;
    --device-frame: #1c1c1e;
    --map-land: #c9c7c0;
    --map-sea: #a8c4dc;
    --help-green: #56b82c;
    --button-border: #cfcfcf;
  }
  * { box-sizing: border-box; margin: 0; padding: 0; }
  html, body { width: 1200px; height: 835px; overflow: hidden; background: var(--white); }
  body { position: relative; font-family: "Space Mono", monospace; color: var(--ink); }

  .site-header { position: absolute; left: 0; top: 0; width: 1200px; height: 70px; background: var(--white); }
  .brand { position: absolute; left: 186px; top: 16px; font-family: "Space Mono", monospace; font-weight: 700; font-size: 28px; line-height: 38px; color: var(--ink); }
  .auth-nav { position: absolute; top: 22px; left: 869px; display: flex; gap: 7px; }
  .auth-button { display: flex; align-items: center; justify-content: center; width: 84px; height: 29px; font-family: "Montserrat", sans-serif; font-weight: 500; font-size: 13px; text-decoration: none; }
  .auth-button--signup { background: var(--signup-green); color: var(--white); }
  .auth-button--login { background: var(--white); color: var(--ink); border: 1px solid var(--button-border); }

  .hero { position: absolute; left: 0; top: 70px; width: 1200px; height: 566px; overflow: hidden;
    background: radial-gradient(ellipse 70% 80% at 50% 40%, var(--brand-blue) 0%, var(--brand-blue-deep) 70%, var(--brand-blue-edge) 100%); }
  .hero-title { position: absolute; top: 64px; width: 100%; text-align: center; color: var(--white); font-weight: 400; font-size: 42px; line-height: 60px; letter-spacing: -0.5px; }
  .search-form { position: absolute; left: 317px; top: 158px; width: 577px; height: 46px; background: var(--field-bg); border: 2px solid #2b7fae; display: flex; }
  .search-input { flex: 1; border: 0; background: transparent; padding: 0 13px; font-family: "Space Mono", monospace; font-size: 18px; color: #222; }
  .search-input::placeholder { color: #222; }
  .search-locate { width: 46px; border: 0; border-left: 1px solid #cdd9e2; display: flex; align-items: center; justify-content: center; background: transparent; }

  .laptop { position: absolute; left: 396px; top: 258px; width: 520px; height: 340px; background: var(--device-frame); border-radius: 12px 12px 0 0; overflow: hidden; }
  .laptop-screen { position: absolute; left: 12px; top: 24px; width: 486px; height: 300px;
    background: linear-gradient(100deg, var(--map-land) 0%, #d2cfc6 55%, var(--map-sea) 72%, #b5cde0 100%); }
  .laptop-glare { position: absolute; left: 0; top: 0; width: 520px; height: 340px;
    background: linear-gradient(112deg, transparent 0%, transparent 42%, rgba(255,255,255,0.14) 42.2%, rgba(255,255,255,0.08) 100%); }
  .phone { position: absolute; left: 268px; top: 362px; width: 164px; height: 240px; background: var(--device-frame); border-radius: 20px 20px 0 0; }
  .phone-screen { position: absolute; left: 8px; top: 56px; width: 148px; height: 190px; overflow: hidden;
    background: linear-gradient(115deg, var(--screen-green) 0%, var(--screen-green) 62%, var(--screen-green-light) 62.5%, var(--screen-green-light) 100%); }
  .phone-name { position: absolute; top: 26px; width: 100%; text-align: center; font-family: "Space Mono", monospace; font-weight: 700; font-size: 14px; color: var(--white); }
  .phone-art { position: absolute; left: 40px; top: 68px; width: 68px; height: 68px; border-radius: 50%; background: #3f8f22; }

  .signup-callout { position: absolute; left: 251px; top: 244px; width: 156px; height: 156px; background: var(--callout-pink); color: var(--white); text-align: center; font-size: 23px; line-height: 23px; padding-top: 22px; text-decoration: none; }
  .signup-callout::after { content: ""; position: absolute; left: 56px; bottom: -42px; border-left: 20px solid transparent; border-right: 20px solid transparent; border-top: 42px solid var(--callout-pink); }

  .site-footer { position: absolute; left: 0; top: 636px; width: 1200px; height: 199px; background: var(--white); }
  .footer-nav { position: absolute; top: 42px; left: 0; width: 1200px; }
  .footer-link { position: absolute; transform: translateX(-50%); font-size: 13px; color: var(--ink); text-decoration: none; }
  .footer-link--active { color: var(--help-green); }
  .copyright { position: absolute; top: 74px; width: 100%; text-align: center; font-family: "Montserrat", sans-serif; font-weight: 500; font-size: 13px; }
</style>
</head>
<body>
  <header class="site-header">
    <div class="brand">WOZZLENT</div>
    <nav class="auth-nav">
      <a class="auth-button auth-button--signup" href="#">signup</a>
      <a class="auth-button auth-button--login" href="#">login</a>
    </nav>
  </header>

  <main class="hero">
    <h1 class="hero-title">Who would you like to find?</h1>
    <form class="search-form">
      <input class="search-input" type="text" placeholder="Search by artist or keyword...">
      <button class="search-locate" type="button" aria-label="Search near my location">
        <svg width="30" height="30" viewBox="0 0 30 30">
          <circle cx="13" cy="16" r="10" fill="none" stroke="#1d5f86" stroke-width="2"/>
          <ellipse cx="13" cy="16" rx="4.5" ry="10" fill="none" stroke="#1d5f86" stroke-width="2"/>
          <line x1="3" y1="16" x2="23" y2="16" stroke="#1d5f86" stroke-width="2"/>
          <line x1="5" y1="11" x2="21" y2="11" stroke="#1d5f86" stroke-width="1.6"/>
          <line x1="5" y1="21" x2="21" y2="21" stroke="#1d5f86" stroke-width="1.6"/>
          <path d="M23 2a4 4 0 0 1 4 4c0 3-4 7-4 7s-4-4-4-7a4 4 0 0 1 4-4z" fill="#f0155f"/>
          <circle cx="23" cy="6" r="1.4" fill="#fff"/>
        </svg>
      </button>
    </form>

    <div class="laptop">
      <div class="laptop-screen" role="img" aria-label="Map of East Asia showing cities and coastline"></div>
      <div class="laptop-glare"></div>
    </div>
    <div class="phone">
      <div class="phone-screen">
        <div class="phone-name">WOZZLENT</div>
        <div class="phone-art" role="img" aria-label="Illustration of a hand holding a phone"></div>
      </div>
    </div>
    <a class="signup-callout" href="#">not a<br>member<br>yet?<br>signup<br>now.</a>
  </main>

  <footer class="site-footer">
    <nav class="footer-nav">
      <a class="footer-link" style="left:274px" href="#">About</a>
      <a class="footer-link footer-link--active" style="left:374px" href="#">Help</a>
      <a class="footer-link" style="left:484px" href="#">Contact</a>
      <a class="footer-link" style="left:604px" href="#">Privacy</a>
      <a class="footer-link" style="left:716px" href="#">Terms</a>
      <a class="footer-link" style="left:828px" href="#">Refunds</a>
      <a class="footer-link" style="left:933px" href="#">Faq</a>
    </nav>
    <p class="copyright">© 2014 Wozzlent-example.com All rights reserved.</p>
  </footer>
</body>
</html>
```